Web Design Project - for professional writing website

This website is a shop-front for a professional writing company. The company specialises in writing resumes, cover letters and other personal career documents, such as Brightvane profiles. It also performs a range of other professional writing services, such as technical writing and tender documents.

Customers use the site to get information about career documents, find out about our approach and order online.

The key brand idea that needs to come across is craftsmanship, in the sense of old-fashioned ideas of skilled trades. The working title business name is The Copper Gate and I would like the graphic design of the site to draw inspiration from old-school trades and craftspeople, like blacksmiths.

I will be programming the site myself in Joomla.

Some websites I like:

Some joomla templates I might be using to build the site.

I'd be interested to see a work in progress so I can provide more guidance.

Reason: Still looking for submissions from a range of designers.

Target Market(s)

Australian workers, particularly white-collar professionals

Industry/Entity Type

Graphic Design

Requirements
Must have
• Each page must have space on either the right or left-hand side for a contact for and live chat button.
Nice to have
• One current idea is to have the site primarily black and white (with some strategic use of colour to keep it interesting) and to use imagery of wrought iron however I am open to alternatives.
Should not have
• No Arial in the fonts
No cartoons in the graphics

```html
<!DOCTYPE html>
<html lang="en">
<head>
<meta charset="utf-8">
<title>The Copper Gate</title>
<link rel="stylesheet" href="https://fonts.googleapis.com/css2?family=Questrial&family=Mulish:wght@400;600;700&display=swap">
<style>
:root{
  --ink:#111111;
  --text:#2b2b2b;
  --orange:#ef8a17;
  --orange-dark:#d97706;
  --rule:#d6d6d6;
  --hero-top:#ececec;
  --hero-bottom:#fafafa;
  --panel:#e6e6e6;
  --footer:#414141;
  --white:#ffffff;
}
*{box-sizing:border-box;margin:0;padding:0}
html,body{width:861px;height:1200px;overflow:hidden;background:var(--white)}
body{position:relative;font-family:"Mulish",sans-serif;color:var(--text)}
.abs{position:absolute}
.display{font-family:"Questrial",sans-serif;color:var(--ink)}

.topbar{left:0;top:0;width:861px;height:5px;background:var(--ink)}
.util-tab{left:628px;top:5px;width:195px;height:32px;background:#f4f4f4;border:1px solid #dcdcdc;border-top:0;border-radius:0 0 5px 5px;display:flex;align-items:center;justify-content:center;gap:16px;font-size:11px;color:#333}
.util-tab span{display:flex;align-items:center;gap:6px}

.brand{left:28px;top:40px;display:flex;align-items:center;gap:8px;font-family:"Questrial",sans-serif;font-size:18px;color:var(--ink);line-height:1}
.brand i{display:block;width:12px;height:12px;background:var(--ink)}

.nav{left:341px;top:79px;display:flex;align-items:center;height:30px;font-family:"Questrial",sans-serif;font-size:11.5px;color:#222}
.nav a{color:inherit;text-decoration:none;padding:0 14px;line-height:14px;border-left:1px solid #888}
.nav a.first{border-left:0}
.nav a.current{background:var(--orange);color:var(--white);line-height:30px;padding:0 18px;border:0}
.nav a.current + a{border-left:0}
.header-rule{left:0;top:127px;width:861px;height:1px;background:var(--rule)}

.hero{left:0;top:128px;width:861px;height:300px;background:linear-gradient(var(--hero-top),var(--hero-bottom))}
.hero-title{left:60px;top:176px;font-size:23px;letter-spacing:.5px}
.hero-sub{left:60px;top:207px;font-size:16px}
.hero-copy{left:60px;top:234px;width:240px;font-size:9.3px;line-height:15px}
.btn-dark{left:60px;top:321px;width:95px;height:30px;background:#1b1b1b;border-radius:3px;color:var(--white);font-size:11.5px;display:flex;align-items:center;justify-content:center;gap:6px}
.slide-arrow{top:241px;width:27px;height:46px;background:#3a3a3a;display:flex;align-items:center;justify-content:center}
.gate-art{left:335px;top:165px;width:470px;height:223px;background:linear-gradient(#f0f0f0,#dadada);border-radius:2px}

.feature{top:460px;width:260px}
.feature-icon{position:absolute;left:0;top:0}
.feature h3{position:absolute;left:54px;top:6px;font-family:"Questrial",sans-serif;font-weight:400;font-size:17px;color:var(--ink);white-space:nowrap}
.feature .tag{position:absolute;left:54px;top:28px;font-size:10.5px;color:#333}
.feature p{position:absolute;left:0;top:54px;width:255px;font-size:9.3px;line-height:15px}
.btn-orange{position:absolute;background:var(--orange);color:var(--white);font-size:10.5px;font-weight:600;display:flex;align-items:center;justify-content:center;gap:6px;border-radius:2px;box-shadow:0 1px 0 var(--orange-dark)}
.feature .btn-orange{left:0;top:140px;width:91px;height:28px}
.dots{top:460px;width:0;height:170px;border-left:1px dotted #999}
.feature-rule{left:0;top:648px;width:861px;height:1px;background:var(--rule)}

.welcome-title{left:32px;top:676px;font-size:15px}
.welcome-copy{left:32px;top:700px;width:552px;font-size:8.6px;line-height:15px}
.welcome-copy p+p{margin-top:15px}
.sample{top:858px;width:257px}
.sample-doc{width:257px;height:104px;background:linear-gradient(#ffffff,#f3f3f3);border:1px solid #cfcfcf;box-shadow:0 1px 2px rgba(0,0,0,.15)}
.sample h4{margin-top:13px;font-family:"Questrial",sans-serif;font-weight:400;font-size:13px;color:var(--ink)}
.sample p{margin-top:6px;font-size:8.6px;line-height:15px;width:257px}
.sample .btn-orange{position:static;width:72px;height:21px;margin-top:9px;font-weight:400}

.side-card{left:608px;width:238px;height:127px;background:var(--panel);padding:5px}
.side-inner{position:relative;width:100%;height:100%;background:var(--white);border:1px solid #d0d0d0}
.side-inner h5{position:absolute;left:19px;top:12px;font-family:"Questrial",sans-serif;font-weight:400;font-size:15px;color:var(--orange)}
.side-inner p{position:absolute;left:19px;top:36px;width:128px;font-size:8.4px;line-height:13px;color:#333}
.side-inner .btn-orange{left:19px;top:82px;width:71px;height:20px;font-weight:400;font-size:10px}
.side-inner svg{position:absolute;right:16px;top:16px}

.footer{left:0;top:1113px;width:861px;height:87px;background:var(--footer);color:#f0f0f0}
.footer-links{position:absolute;left:22px;top:23px;font-size:9.5px}
.footer-links span{padding:0 4px;color:#bbb}
.footer-legal{position:absolute;left:22px;top:51px;font-size:8.3px}
.footer-legal span{padding:0 4px;color:#bbb}
</style>
</head>
<body>
<div class="abs topbar"></div>
<div class="abs util-tab">
  <span><svg width="20" height="16" viewBox="0 0 20 16"><path d="M1 1h18v10H8l-4 4v-4H1z" fill="var(--orange)"/></svg>Live Chat</span>
  <span><svg width="22" height="15" viewBox="0 0 22 15"><rect x="1" y="1" width="20" height="13" fill="none" stroke="#999"/><path d="M1 1l10 8 10-8" fill="none" stroke="#999"/></svg>Contact us</span>
</div>

<div class="abs brand"><i></i>The Copper Gate</div>

<nav class="abs nav">
  <a class="current">HOME</a>
  <a>ABOUT US</a>
  <a>GET DOCUMENTS</a>
  <a>INFORMATION</a>
  <a>BLOG</a>
  <a>CONTACT</a>
</nav>
<div class="abs header-rule"></div>

<section class="abs hero"></section>
<h1 class="abs display hero-title" style="font-weight:400">THE COPPER GATE</h1>
<h2 class="abs display hero-sub" style="font-weight:400">Punch line goes here</h2>
<p class="abs hero-copy">Northwell Studio is specialized in handling advanced web projects and the ongoing projects that require permanent maintenance and support .We like challenges and do complete these challenge with expertise we like solving questions that arises.</p>
<div class="abs btn-dark">Learn more <span>›</span></div>
<div class="abs slide-arrow" style="left:0"><svg width="10" height="14" viewBox="0 0 10 14"><path d="M8 1L2 7l6 6" fill="none" stroke="#fff" stroke-width="2.4"/></svg></div>
<div class="abs slide-arrow" style="left:834px"><svg width="10" height="14" viewBox="0 0 10 14"><path d="M2 1l6 6-6 6" fill="none" stroke="#fff" stroke-width="2.4"/></svg></div>
<div class="abs gate-art" role="img" aria-label="Black wrought iron double gate with arched top rails and spear finials"></div>

<div class="abs feature" style="left:40px">
  <svg class="feature-icon" width="40" height="42" viewBox="0 0 40 42"><path d="M14 2h12l13 38h-9l-3-9H13l-3 9H1z M16 23h8l-4-13z" fill="var(--orange)" fill-rule="evenodd"/></svg>
  <h3>Featured Letters</h3><div class="tag">tittle line goes here</div>
  <p>Northwell Studio is specialized in handling advanced web projects and the ongoing projects that require permanent maintenance and support .We like challenges and do complete these challenge with expertise we like solving questions</p>
  <div class="btn-orange" style="top:140px">VIEW MORE <span>›</span></div>
</div>
<div class="abs dots" style="left:296px"></div>
<div class="abs feature" style="left:317px">
  <svg class="feature-icon" width="40" height="40" viewBox="0 0 40 40"><rect x="2" y="6" width="30" height="32" rx="3" fill="var(--orange)"/><path d="M12 28l3-8 16-16 5 5-16 16z" fill="#fff"/><path d="M14 27l2-6 4 4z" fill="var(--orange)"/></svg>
  <h3>Featured Resume</h3><div class="tag">tittle line goes here</div>
  <p>Northwell Studio is specialized in handling advanced web projects and the ongoing projects that require permanent maintenance and support .We like challenges and do complete these challenge with expertise we like solving questions</p>
  <div class="btn-orange" style="top:138px">VIEW MORE <span>›</span></div>
</div>
<div class="abs dots" style="left:574px"></div>
<div class="abs feature" style="left:597px">
  <svg class="feature-icon" width="50" height="40" viewBox="0 0 50 40"><rect x="8" y="4" width="30" height="30" fill="var(--orange)"/><path d="M14 12h18M14 18h18M14 24h12" stroke="#fff" stroke-width="2.5"/><rect x="2" y="28" width="22" height="6" rx="3" fill="var(--orange)"/><path d="M36 30l10-10" stroke="var(--orange)" stroke-width="3"/></svg>
  <h3 style="left:61px">Featured Document</h3><div class="tag" style="left:61px">tittle line goes here</div>
  <p>Northwell Studio is specialized in handling advanced web projects and the ongoing projects that require permanent maintenance and support .We like challenges and do complete these challenge with expertise we like solving questions</p>
  <div class="btn-orange" style="top:138px">VIEW MORE <span>›</span></div>
</div>
<div class="abs feature-rule"></div>

<h2 class="abs display welcome-title" style="font-weight:400">Welcome to The Copper Gate Website Mainpage</h2>
<div class="abs welcome-copy">
  <p>Northwell Studio provides you the Search Engine Optimization making your website search engine friendly. So that the website can achieve top position and ranking in the Internet searches and thereby increasing the scope for the website to be found by customers. We here modify the site to improve the ranking by using the keywords and contents.</p>
  <p>E-Commerce is a major progress in technology that has changed the way in which the customers now purchase information, products and the services. It’s the new way of providing an opportunity to make your products and services available in the global market 24 hours a day through Internet. Northwell Studio is specialized in handling advanced web projects and the ongoing projects that require permanent maintenance and support .We like challenges and do complete these challenge with expertise we like solving questions that arises in such projects as these helps us to grow also.</p>
</div>

<div class="abs sample" style="left:32px">
  <div class="sample-doc" role="img" aria-label="Sample resume page preview"></div>
  <h4>Sample goes here</h4>
  <p>Northwell Studio provides you the Search Engine Optimization making your website search engine friendly. So that the website can achieve top position and ranking in the Internet</p>
  <div class="btn-orange">VIEW MORE</div>
</div>
<div class="abs sample" style="left:313px">
  <div class="sample-doc" role="img" aria-label="Resume format template preview"></div>
  <h4>Sample goes here</h4>
  <p>Northwell Studio provides you the Search Engine Optimization making your website search engine friendly. So that the website can achieve top position and ranking in the Internet</p>
  <div class="btn-orange">VIEW MORE</div>
</div>

<aside class="abs side-card" style="top:672px"><div class="side-inner">
  <h5>Quick Contact</h5>
  <p>Contact companies with fewer budgets can promote their products and services through</p>
  <div class="btn-orange">CLICK HERE</div>
  <svg width="58" height="48" viewBox="0 0 58 48"><path d="M2 20L29 2l27 18v26H2z" fill="#111"/><rect x="12" y="10" width="34" height="22" fill="#fff"/><path d="M20 16h18M20 21h18M20 26h12" stroke="#111" stroke-width="2"/><path d="M2 20l27 18 27-18v26H2z" fill="#111" stroke="#fff" stroke-width="2"/></svg>
</div></aside>
<aside class="abs side-card" style="top:811px"><div class="side-inner">
  <h5>Chat Now</h5>
  <p>Chat companies with fewer budts can promote their products and services through</p>
  <div class="btn-orange">CLICK HERE</div>
  <svg width="54" height="54" viewBox="0 0 54 54"><circle cx="27" cy="27" r="26" fill="#111"/><path d="M14 28c0-8 6-13 14-13s13 5 13 12-6 12-14 12c-3 0-5 0-7-1l-7 3 2-6c-1-2-1-4-1-7z" fill="#fff"/></svg>
</div></aside>
<aside class="abs side-card" style="top:950px"><div class="side-inner">
  <h5>Download</h5>
  <p>Chat companies with fewer budts can promote their products and services through</p>
  <div class="btn-orange">CLICK HERE</div>
  <svg width="54" height="54" viewBox="0 0 54 54"><circle cx="27" cy="27" r="26" fill="#111"/><circle cx="27" cy="27" r="21" fill="none" stroke="#fff" stroke-width="2"/><path d="M22 12h10v14h8L27 42 14 26h8z" fill="#fff"/></svg>
</div></aside>

<footer class="abs footer">
  <div class="footer-links">Home<span>|</span>About Us<span>|</span>Documents<span>|</span>Information<span>|</span>Dowload<span>|</span>Blog<span>|</span>Contact Us<span>|</span>FAQ<span>|</span>Support<span>|</span>Term of Use</div>
  <div class="footer-legal">© 2012 Company Name<span>|</span>All right reserved<span>|</span>Term &amp; Conditions</div>
</footer>
</body>
</html>
```